Bourbon label design for bourbon brand. Looking to freshen our current label.

I need a Bourbon label design for our rebranded Bourbon bottle. Label should include picture of our horse and our logo on the bottle. Front Label is 3.5 inches wide and 6 inches tall, back label is 4 inches tall and 3 inches wide. Back label can be a simple plain logo like the one in the brief. I have included a design of our current bottle and label. We want to stay close to the current color schemes but want a fresh rebrand of the design. The label needs to be the correct size on a tall bottle like pictured.

Target Market(s)

Our Bourbon members, 30-50 year old males

Requirements
Must have
• Picture of our horse, our B logo , straight Bourbon whiskey on the front. Room to edit text on the back label.

```html
<!DOCTYPE html>
<html lang="en">
<head>
<meta charset="utf-8">
<title>Nightfall Straight Bourbon Whiskey – Labels</title>
<link href="https://fonts.googleapis.com/css2?family=Sancreek&family=Roboto+Condensed:wght@700&family=Montserrat:wght@400;500&display=swap" rel="stylesheet">
<style>
  :root {
    --paper: #ffffff;
    --label-black: #000000;
    --ink-white: #ffffff;
    --ink-grey: #d9d9d9;
    --gold: #c9a86a;
    --gold-soft: #8a7448;
    --box-white: #ffffff;
  }
  * { margin: 0; padding: 0; box-sizing: border-box; }
  html, body { width: 1200px; height: 1200px; overflow: hidden; background: var(--paper); }
  .canvas { position: relative; width: 1200px; height: 1200px; }

  /* ---------- Front label ---------- */
  .front-label {
    position: absolute; left: 120px; top: 223px;
    width: 440px; height: 754px;
    background: var(--label-black);
    color: var(--ink-white);
    font-family: "Sancreek", serif;
  }
  .front-label .horse-art {
    position: absolute; left: 95px; top: 37px; width: 250px; height: 320px;
    background: radial-gradient(ellipse at 50% 45%, #e8e8e8 0%, #9a9a9a 35%, #3a3a3a 65%, #000 85%);
  }
  .est-mark {
    position: absolute; top: 160px; width: 80px; text-align: center;
    font-size: 22px; color: var(--ink-grey);
  }
  .est-mark::before, .est-mark::after {
    content: ""; position: absolute; left: 0; right: 0; height: 1px;
    background: linear-gradient(90deg, transparent, var(--gold), transparent);
  }
  .est-mark::before { top: -2px; }
  .est-mark::after { bottom: -2px; }
  .est-mark.left { left: 34px; }
  .est-mark.right { right: 34px; }

  .brand-title {
    position: absolute; left: 0; right: 0; top: 346px; text-align: center;
    font-size: 92px; line-height: 1; letter-spacing: 1px;
  }
  .brand-subtitle {
    position: absolute; left: 0; right: 0; top: 446px; text-align: center;
    font-size: 30px; line-height: 1; letter-spacing: 0.5px;
  }
  .brand-name-mark {
    position: absolute; left: 0; right: 0; top: 508px;
    display: flex; align-items: center; justify-content: center; gap: 8px;
    font-size: 24px;
  }
  .brand-name-mark .dot {
    width: 14px; height: 14px; border-radius: 50%; background: var(--ink-white);
  }
  .side-note {
    position: absolute; top: 527px; width: 90px; text-align: center;
    font-size: 13px; line-height: 1;
  }
  .side-note.left { left: 42px; }
  .side-note.right { right: 42px; }

  .series-line {
    position: absolute; left: 0; right: 0; top: 588px;
    display: flex; align-items: center; justify-content: center; gap: 8px;
    font-size: 20px; color: var(--ink-grey);
  }
  .series-line .rule {
    width: 80px; height: 5px;
    border-top: 1px solid var(--gold); border-bottom: 1px solid var(--gold-soft);
  }
  .spec-row {
    position: absolute; left: 0; right: 0; top: 620px;
    display: flex; justify-content: space-around; padding: 0 34px;
  }
  .spec { width: 70px; text-align: center; font-size: 16px; }
  .spec .fill-box { margin-top: 4px; height: 42px; background: var(--box-white); }
  .spec .unit { margin-top: 6px; font-size: 16px; }
  .volume {
    position: absolute; left: 0; right: 0; top: 730px; text-align: center; font-size: 17px;
  }

  /* ---------- Back label ---------- */
  .back-label {
    position: absolute; left: 680px; top: 349px;
    width: 376px; height: 502px;
    background: var(--label-black);
    color: var(--ink-white);
    font-family: "Roboto Condensed", sans-serif; font-weight: 700;
    text-align: center;
    display: flex; flex-direction: column; align-items: center;
    padding-top: 30px;
  }
  .company-mark {
    display: flex; align-items: center; gap: 6px;
    font-family: "Montserrat", sans-serif; font-weight: 500;
    font-size: 15px; line-height: 1.1; letter-spacing: 0.5px;
  }
  .company-mark .dot { width: 12px; height: 12px; border-radius: 50%; background: var(--ink-white); }
  .company-tag {
    margin-top: 3px; font-family: "Montserrat", sans-serif; font-weight: 400;
    font-size: 7px; letter-spacing: 4px;
  }
  .edition-title { margin-top: 18px; font-size: 17px; line-height: 1.2; }
  .edition-story { margin-top: 10px; font-size: 10.5px; line-height: 1.42; padding: 0 26px; }
  .bottler { margin-top: 14px; font-size: 10.5px; line-height: 1.42; }
  .site { margin-top: 14px; font-size: 18px; line-height: 1.15; }
  .gov-warning {
    margin-top: 14px; padding: 0 48px; text-align: justify;
    font-family: "Montserrat", sans-serif; font-weight: 400;
    font-size: 8px; line-height: 1.65; letter-spacing: 0.6px;
  }
  .gov-warning strong { font-weight: 500; letter-spacing: 1.2px; }
</style>
</head>
<body>
<div class="canvas">

  <section class="front-label" aria-label="Front label">
    <div class="horse-art" role="img" aria-label="Black and white painted illustration of the racehorse with jockey charging forward"></div>
    <div class="est-mark left">EST</div>
    <div class="est-mark right">2016</div>
    <h1 class="brand-title">NIGHTFALL</h1>
    <div class="brand-subtitle">STRAIGHT BOURBON WHISKEY</div>
    <div class="side-note left">SINGLE<br>BARREL</div>
    <div class="brand-name-mark"><span class="dot"></span><span>NIGHTFALL</span></div>
    <div class="side-note right">STRAIGHT<br>BARREL</div>
    <div class="series-line"><span class="rule"></span><span>WINNERS SERIES</span><span class="rule"></span></div>
    <div class="spec-row">
      <div class="spec">BARREL<div class="fill-box"></div></div>
      <div class="spec">AGED<div class="fill-box"></div><div class="unit">YEARS</div></div>
      <div class="spec">ALC/VOL<div class="fill-box"></div></div>
    </div>
    <div class="volume">750ML</div>
  </section>

  <section class="back-label" aria-label="Back label">
    <div class="company-mark"><span class="dot"></span><span>NIGHTFALL<br>BARREL</span></div>
    <div class="company-tag">COMPANY</div>
    <h2 class="edition-title">Winners Séries<br>Silver Verdict Edition<br>Single Barrel No. 45</h2>
    <p class="edition-story">The Nightfall Racing Winners Series honors the horses who have brought home victories for our stable. This editions celebrates Silver Verdict and her maiden victory on May 28, 2021. Raise a glass to her incredible career with this non chill filtered single barrel crafted in her honor.<br>Here’s to Silver Verdict - a true champions!</p>
    <p class="bottler">Bottled by Riverbend Whiskey Co., Louisville Kentucky<br>Distilled in Bardstown, Kentucky</p>
    <p class="site">NIGHTFALL-GROUP.EXAMPLE<br>750ml.</p>
    <p class="gov-warning"><strong>GOVERNMENT WARNING:</strong> (1) According to the Surgeon General, women should not drink alcoholic beverages during pregnancy because of the risk of birth defects. (2) Consumption of alcoholic beverages impairs your ability to drive a car or operate machinery, and may cause health problems.</p>
  </section>

</div>
</body>
</html>
```